Bramwick Client Journey To Success

I need a one-page document that graphically shows the client's journey working with Bramwick from initial assessment to completed project. I want the journey to start at the "basecamp logo" and reach 4 summits (little mountain logos...) .

I'd like the imagery to convey the client starting at basecamp, and moving to each summit. Each summit, should list the subtext under each, as listed on the pdf doc i provided.

The description for the basecamp and 4 summits is attached.

I need the brochure to look like the other brochure that you did for me (attached) .

Target Market(s)

Restaurant Owners

Industry/Entity Type

Construction Management

Font styles to use
Sans Serif

Colors
EB3D1F
EC4F4E
F09395
F8D3D4
FCEDEE

Requirements
Must have
• My logo. Title: Client Journey To Success. Subtitle: The 4 Summits

```html
<!DOCTYPE html>
<html lang="en">
<head>
<meta charset="utf-8">
<title>Bramwick Development Services – Client Journey</title>
<link href="https://fonts.googleapis.com/css2?family=Anton&family=Montserrat:wght@400;500;600;700;800&display=swap" rel="stylesheet">
<style>
  :root {
    --red: #d0262b;
    --red-light: #e03a3c;
    --ink: #262626;
    --ink-soft: #3a3a3a;
    --panel: #f0f0f0;
    --page: #ffffff;
    --footer: #2a2a2a;
  }
  * { margin: 0; padding: 0; box-sizing: border-box; }
  html, body { width: 800px; height: 1200px; overflow: hidden; background: var(--page); }
  .poster {
    position: relative; width: 800px; height: 1200px; background: var(--page);
    font-family: "Montserrat", Arial, sans-serif; color: var(--ink);
  }
  .company-title {
    position: absolute; top: 64px; left: 0; width: 800px; text-align: center;
    font-family: "Anton", "Oswald", sans-serif; font-size: 48px; font-weight: 400; letter-spacing: -0.5px;
    color: var(--ink); line-height: 1; white-space: nowrap;
  }
  .ribbon { position: absolute; top: 136px; left: 189px; width: 394px; height: 50px; }
  .ribbon-text {
    position: absolute; top: 136px; left: 189px; width: 394px; height: 50px;
    display: flex; align-items: center; justify-content: center;
    color: #fff; font-weight: 700; font-size: 25px; letter-spacing: 1.5px;
  }
  .journey-panel { position: absolute; top: 227px; left: 22px; width: 751px; height: 863px; background: var(--panel); }
  .headline {
    position: absolute; top: 262px; left: 248px;
    font-weight: 700; font-size: 86px; color: var(--red); letter-spacing: 2px; line-height: 1;
  }
  .art { position: absolute; top: 0; left: 0; width: 800px; height: 1200px; }
  .stage { position: absolute; }
  .stage-title { font-weight: 800; font-size: 28px; line-height: 1.1; letter-spacing: 0.3px; white-space: nowrap; }
  .stage-title.red { color: var(--red); }
  .stage-sub { font-weight: 700; font-size: 16px; letter-spacing: 0.6px; margin-top: 4px; white-space: nowrap; }
  .stage-sub.red { color: var(--red); }
  .stage-list { list-style: none; font-size: 12.5px; line-height: 16.5px; margin-top: 8px; color: var(--ink-soft); white-space: nowrap; }
  .basecamp { top: 438px; left: 563px; }
  .summit-1 { top: 582px; left: 55px; }
  .summit-2 { top: 684px; left: 563px; }
  .summit-3-pm { top: 843px; left: 55px; }
  .summit-3-done { top: 954px; left: 563px; }
  .footer-block { position: absolute; top: 1137px; left: 0; width: 47px; height: 63px; background: var(--footer); }
  .brand {
    position: absolute; top: 1148px; left: 55px; width: 125px;
    display: flex; flex-direction: column; align-items: center; gap: 6px;
  }
  .brand-mark { width: 24px; height: 24px; background: var(--red); }
  .brand-name { font-weight: 800; font-size: 8px; letter-spacing: 0.2px; color: var(--ink); white-space: nowrap; line-height: 1; }
  .contact-bar {
    position: absolute; top: 1143px; left: 183px; width: 617px; height: 57px; background: var(--footer);
    display: flex; align-items: center; gap: 22px; padding-left: 18px; color: #fff;
  }
  .contact { display: flex; align-items: center; gap: 10px; font-size: 25px; font-weight: 400; white-space: nowrap; }
  .contact.web { font-size: 22px; }
</style>
</head>
<body>
<div class="poster">
  <h1 class="company-title">BRAMWICK DEVELOPMENT SERVICES, LLC</h1>
  <svg class="ribbon" viewBox="0 0 394 50" aria-hidden="true">
    <polygon points="0,0 394,0 380,25 394,50 0,50 14,25" fill="var(--red)"/>
  </svg>
  <div class="ribbon-text">WITH CLIENT JOURNEY</div>

  <div class="journey-panel"></div>

  <svg class="art" viewBox="0 0 800 1200" aria-hidden="true">
    <defs>
      <polygon id="hex-outer" points="0,-66 57.2,-33 57.2,33 0,66 -57.2,33 -57.2,-33"/>
      <polygon id="hex-mid" points="0,-58 50.2,-29 50.2,29 0,58 -50.2,29 -50.2,-29"/>
      <polygon id="hex-inner" points="0,-51 44.2,-25.5 44.2,25.5 0,51 -44.2,25.5 -44.2,-25.5"/>
    </defs>

    <g transform="translate(180,314)">
      <polygon points="0,-58 50,-29 50,29 0,58 -50,29 -50,-29" fill="var(--red)"/>
      <text x="0" y="28" text-anchor="middle" font-family="Montserrat, sans-serif" font-weight="500" font-size="78" fill="#fff">4</text>
    </g>

    <line x1="410" y1="451" x2="555" y2="451" stroke="var(--ink)" stroke-width="3"/>
    <line x1="242" y1="598" x2="370" y2="598" stroke="var(--red)" stroke-width="3"/>
    <line x1="420" y1="736" x2="560" y2="736" stroke="var(--ink)" stroke-width="3"/>
    <line x1="244" y1="860" x2="378" y2="860" stroke="var(--red)" stroke-width="3"/>
    <line x1="420" y1="985" x2="560" y2="985" stroke="var(--ink)" stroke-width="3"/>

    <g transform="translate(366,1009)">
      <use href="#hex-outer" fill="var(--ink)"/><use href="#hex-mid" fill="#fff"/><use href="#hex-inner" fill="var(--ink)"/>
      <circle cx="4" cy="-14" r="11" fill="#fff"/>
      <path d="M-2,-14 l4,4 l8,-8" stroke="var(--ink)" stroke-width="3" fill="none"/>
      <path d="M-24,18 q10,-12 24,-6 l14,-2 q4,3 0,6 l-14,2 m14,0 l12,-8 q5,2 2,7 l-16,11 h-22" stroke="#fff" stroke-width="3.5" fill="none" stroke-linejoin="round"/>
    </g>
    <g transform="translate(433,879)">
      <use href="#hex-outer" fill="var(--ink)"/><use href="#hex-mid" fill="#fff"/><use href="#hex-inner" fill="var(--red)"/>
      <rect x="-6" y="-20" width="26" height="36" rx="2" fill="#fff"/>
      <path d="M-1,-10 h16 M-1,-3 h16 M-1,4 h16 M-1,10 h10" stroke="var(--red)" stroke-width="2.5"/>
      <circle cx="-14" cy="0" r="11" fill="none" stroke="#fff" stroke-width="5" stroke-dasharray="4 3"/>
    </g>
    <g transform="translate(366,749)">
      <use href="#hex-outer" fill="var(--ink)"/><use href="#hex-mid" fill="#fff"/><use href="#hex-inner" fill="var(--ink)"/>
      <rect x="-20" y="-22" width="32" height="42" rx="3" fill="#fff"/>
      <rect x="-10" y="-26" width="12" height="8" rx="2" fill="#fff"/>
      <path d="M-15,-10 l3,3 l5,-5 M-15,1 l3,3 l5,-5 M-15,12 l3,3 l5,-5" stroke="var(--ink)" stroke-width="2.2" fill="none"/>
      <path d="M2,-6 h6 M2,5 h6" stroke="var(--ink)" stroke-width="2.2"/>
      <path d="M4,18 l18,-22 l6,5 l-18,22 l-8,3 z" fill="#fff" stroke="var(--ink)" stroke-width="2"/>
    </g>
    <g transform="translate(425,619)">
      <use href="#hex-outer" fill="var(--ink)"/><use href="#hex-mid" fill="#fff"/><use href="#hex-inner" fill="var(--red)"/>
      <circle cx="-12" cy="-18" r="5" fill="#fff"/><circle cx="0" cy="-21" r="6" fill="#fff"/><circle cx="12" cy="-18" r="5" fill="#fff"/>
      <path d="M-20,-4 q8,-10 40,0 z" fill="#fff"/>
      <circle cx="0" cy="12" r="13" fill="none" stroke="#fff" stroke-width="7" stroke-dasharray="5 3.2"/>
      <circle cx="0" cy="12" r="5" fill="var(--red)"/>
    </g>
    <g transform="translate(366,489)">
      <use href="#hex-outer" fill="var(--ink)"/><use href="#hex-mid" fill="#fff"/><use href="#hex-inner" fill="var(--ink)"/>
      <circle cx="0" cy="0" r="19" fill="none" stroke="#fff" stroke-width="8" stroke-dasharray="6 4.5"/>
      <circle cx="0" cy="0" r="14" fill="#fff"/>
      <circle cx="0" cy="0" r="9" fill="var(--ink)"/>
      <path d="M-4,0 l3,3 l5,-6" stroke="#fff" stroke-width="2" fill="none"/>
    </g>

    <g font-family="Montserrat, sans-serif" font-weight="700" font-size="18" fill="#fff" text-anchor="middle">
      <circle cx="400" cy="451" r="19" fill="var(--ink)" stroke="#fff" stroke-width="3"/><text x="400" y="457">01</text>
      <circle cx="388" cy="598" r="19" fill="var(--ink)" stroke="#fff" stroke-width="3"/><text x="388" y="604">02</text>
      <circle cx="410" cy="736" r="19" fill="var(--ink)" stroke="#fff" stroke-width="3"/><text x="410" y="742">03</text>
      <circle cx="393" cy="860" r="19" fill="var(--ink)" stroke="#fff" stroke-width="3"/><text x="393" y="866">04</text>
      <circle cx="410" cy="985" r="19" fill="var(--ink)" stroke="#fff" stroke-width="3"/><text x="410" y="991">05</text>
    </g>
  </svg>

  <div class="headline">SUMMITS</div>

  <section class="stage basecamp">
    <h2 class="stage-title">BASECAMP</h2>
    <ul class="stage-list">
      <li>a. Client Assessment</li>
      <li>b. Determine Project Goals</li>
      <li>c. Proposal &amp; Fees</li>
    </ul>
  </section>

  <section class="stage summit-1">
    <h2 class="stage-title red">SUMMIT 1</h2>
    <p class="stage-sub">PRECONSTRUCTION</p>
    <ul class="stage-list">
      <li>a. Develop Project Plan</li>
      <li>b. Develop Risk Assessment &amp; Plan</li>
      <li>c. Devlelop Schedule</li>
      <li>d. Develop Budget</li>
      <li>e. Develop Team</li>
      <li>f. GC, Sub, Consultants Contracts</li>
    </ul>
  </section>

  <section class="stage summit-2">
    <h2 class="stage-title">SUMMIT 2</h2>
    <p class="stage-sub red">EXECUTION</p>
    <ul class="stage-list">
      <li>a. Acquire Permits</li>
      <li>b. PreConstruction Meeting</li>
      <li>c. Project Start</li>
    </ul>
  </section>

  <section class="stage summit-3-pm">
    <h2 class="stage-title red">SUMMIT 3</h2>
    <p class="stage-sub">PROJECT MANAGEMENT</p>
    <ul class="stage-list">
      <li>a. Shared Consciousness Meetings</li>
      <li>b. Pressurized Collaboration</li>
      <li>c. Schedule Management</li>
      <li>d. Run O.O.D.A. Loop</li>
    </ul>
  </section>

  <section class="stage summit-3-done">
    <h2 class="stage-title">SUMMIT 3</h2>
    <p class="stage-sub red">COMPLETION</p>
    <ul class="stage-list">
      <li>a. Closeout</li>
    </ul>
  </section>

  <div class="footer-block"></div>
  <div class="brand">
    <span class="brand-mark"></span>
    <span class="brand-name">BRAMWICK DEVELOPMENT</span>
  </div>
  <div class="contact-bar">
    <span class="contact phone">
      <svg width="22" height="22" viewBox="0 0 24 24" aria-hidden="true"><path d="M6.6 10.8a15 15 0 0 0 6.6 6.6l2.2-2.2a1 1 0 0 1 1-.25 11.4 11.4 0 0 0 3.6.6 1 1 0 0 1 1 1V20a1 1 0 0 1-1 1A17 17 0 0 1 3 4a1 1 0 0 1 1-1h3.5a1 1 0 0 1 1 1c0 1.250.2 2.450.6 3.6a1 1 0 0 1-.25 1z" fill="var(--red-light)"/></svg>
      555-014-2290
    </span>
    <span class="contact web">
      <svg width="22" height="22" viewBox="0 0 24 24" aria-hidden="true"><g fill="none" stroke="var(--red-light)" stroke-width="2"><circle cx="12" cy="12" r="9"/><ellipse cx="12" cy="12" rx="4" ry="9"/><path d="M3 12h18M5 7h14M5 17h14"/></g></svg>
      www.bramwickdev.example
    </span>
  </div>
</div>
</body>
</html>
```